Personal sales brochure for client marketing

I am looking for a brochure in the style of a sales menu to sit in front of clients with. I want 5 different colored columns where clients will choose the right package for them.
Eg.
Package 1 called Book-keeping is a basic package
Package 2 called Insight includes the above but also extra services
Package 3 called Compliance an add on for the above packages
Package 4 Called Professional another add on to the above services
Package 5 called payroll another add on to the above.

I want to sit in front of my clients and discuss the services we provide and allow them to choose from this list and tick the boxes of what they would like. I attach a simple spread sheet as well for guideline.

Target Market(s)

business owners requiring accounting support and advice

Industry/Entity Type

Accounting

Font styles to use
Serif
Sans Serif

Requirements
Must have
• Simple, clear, concise with clear product descriptions in colored boxes that highlight clearly the different options. Must have Logo and contact details. This document need to be our key sales and marketing tool so will need to introduce the business clearly and in a professional manner.
• enquiries@brambertonpartners.example
• 01632 960417
Nice to have
• The design needs to be printable on A1 A3 A4 A5
Should not have
• Pictures and patterns

```html
<!DOCTYPE html>
<html lang="en">
<head>
<meta charset="utf-8">
<title>Packages – Bramberton Partners</title>
<link rel="stylesheet" href="https://fonts.googleapis.com/css2?family=Oswald:wght@700&family=Ubuntu:wght@500;700&family=PT+Sans:wght@400&family=Libre+Baskerville&display=swap">
<style>
:root{
  --ink:#1d1d1d;
  --text:#2a2a2a;
  --muted:#555;
  --green-head:#d2ebbd; --green-head-2:#e0f1cf; --green-stripe:#c6e3ad; --green-body:#e5f2d9; --green-tri:#cde8b4;
  --blue-head:#b2def3; --blue-head-2:#c2e6f6; --blue-stripe:#a9d8ef; --blue-body:#d3ebf7; --blue-tri:#a9dbf0;
  --grey-head:#dadada; --grey-head-2:#e4e4e4; --grey-stripe:#d7d7d7; --grey-body:#ececec; --grey-tri:#d9d9d9;
  --pink-head:#f8d3d9; --pink-head-2:#fadfe3; --pink-stripe:#f7c2ca; --pink-body:#fbe2e6; --pink-tri:#f2a2aa;
  --lilac-head:#d6d3ea; --lilac-head-2:#dedbee; --lilac-stripe:#c7c1df; --lilac-body:#e5e2f1; --lilac-tri:#cbc6e4;
  --accent:#3aa84a;
}
*{margin:0;padding:0;box-sizing:border-box}
html,body{width:1200px;height:1015px;overflow:hidden;background:#fff}
body{position:relative;font-family:"PT Sans",sans-serif;color:var(--text)}
.title{position:absolute;left:41px;top:66px;font-family:"Oswald",sans-serif;font-weight:700;font-size:56px;letter-spacing:1px;color:var(--ink);line-height:1}
.contact{position:absolute;right:214px;top:72px;text-align:right;color:var(--ink)}
.contact .web{font-size:26px;line-height:30px;letter-spacing:.3px}
.contact .line{font-size:16px;line-height:24px;display:flex;justify-content:flex-end;align-items:center;gap:8px}
.contact svg{width:15px;height:15px}
.brand{position:absolute;left:1002px;top:80px;width:160px}
.brand .name{font-family:"Libre Baskerville",serif;font-size:22px;line-height:24px;color:#3a3a3a}
.brand .tag{margin-top:8px;font-size:9.5px;letter-spacing:1.6px;color:#555;text-transform:uppercase}
.intro{position:absolute;left:41px;top:148px;font-size:15.5px;line-height:19.5px;width:700px}
.package{position:absolute;top:206px;width:214px}
.package .head{height:119px;border-radius:5px 5px 0 0;display:flex;align-items:center;justify-content:center;font-family:"Ubuntu",sans-serif;font-weight:700;font-size:26px;color:var(--ink);letter-spacing:.2px}
.package .pointer{display:block;margin:12px auto 0;width:34px;height:28px}
.package .body{position:absolute;top:170px;left:1px;width:212px;height:514px}
.package .stripe{position:absolute;left:0;top:0;width:18px;height:100%}
.package .item{position:absolute;left:32px;width:176px;font-size:15.6px;line-height:18.5px}
.package .item::before{content:"";position:absolute;left:-32px;top:3px;border-left:17px solid rgba(255,255,255,.75);border-top:9px solid transparent;border-bottom:9px solid transparent}
.package .note{position:absolute;left:19px;width:193px;height:50px;padding:5px 0 0 13px;font-size:15.6px;line-height:18.5px;background:linear-gradient(90deg,#fff 0%,rgba(255,255,255,.85) 55%,rgba(255,255,255,0) 100%)}
.note.software{top:388px}
.note.support{top:446px}
.bookkeeping{left:35px}.insight{left:262px}.compliance{left:489px}.professional{left:715px}.payroll{left:941px}
.bookkeeping .head{background:linear-gradient(90deg,var(--green-head),var(--green-head-2))}
.bookkeeping .stripe{background:var(--green-stripe)}
.bookkeeping .body{background:linear-gradient(90deg,var(--green-body),#f1f8ea)}
.insight .head{background:linear-gradient(90deg,var(--blue-head),var(--blue-head-2))}
.insight .stripe{background:var(--blue-stripe)}
.insight .body{background:linear-gradient(90deg,var(--blue-body),#e0f1fa)}
.compliance .head{background:linear-gradient(90deg,var(--grey-head),var(--grey-head-2))}
.compliance .stripe{background:var(--grey-stripe)}
.compliance .body{background:linear-gradient(90deg,var(--grey-body),#f2f2f2)}
.professional .head{background:linear-gradient(90deg,var(--pink-head),var(--pink-head-2))}
.professional .stripe{background:var(--pink-stripe)}
.professional .body{background:linear-gradient(90deg,var(--pink-body),#fce8eb)}
.payroll .head{background:linear-gradient(90deg,var(--lilac-head),var(--lilac-head-2))}
.payroll .stripe{background:var(--lilac-stripe)}
.payroll .body{background:var(--lilac-body)}
.catchup{position:absolute;left:36px;top:912px;font-size:15.5px;line-height:20px;width:1000px}
</style>
</head>
<body>
<h1 class="title">PACKAGES</h1>

<div class="contact">
  <div class="web">www.brambertonpartners.example</div>
  <div class="line"><svg viewBox="0 0 16 16" aria-hidden="true"><rect x="1" y="4" width="14" height="10" fill="none" stroke="#333" stroke-width="1.4"/><path d="M1 4l7 6 7-6" fill="none" stroke="var(--accent)" stroke-width="1.6"/></svg>enquiries@brambertonpartners.example</div>
  <div class="line"><svg viewBox="0 0 16 16" aria-hidden="true"><circle cx="8" cy="8" r="6.8" fill="none" stroke="#777" stroke-width="1"/><path d="M5.5 4.5l1.5 0 .8 2-1 .8c.5 1.2 1.2 1.9 2.4 2.4l.8-1 2 .8v1.5c-3.5.3-6.8-3-6.5-6.5z" fill="#333"/></svg>01632 960417</div>
</div>

<div class="brand">
  <div class="name">Bramberton Partners</div>
  <div class="tag">Accounting &amp; business solutions</div>
</div>

<p class="intro">Every business is different and when we understand your needs we can provide just the services you require for an agreed fee. Our services fall into the following categories:</p>

<section class="package bookkeeping">
  <div class="head">BOOK-KEEPING</div>
  <svg class="pointer" viewBox="0 0 34 28" aria-hidden="true"><path d="M0 0h34L17 28z" fill="var(--green-tri)"/></svg>
  <div class="body">
    <div class="stripe"></div>
    <div class="item" style="top:36px">Monthly/Quarterly/<br>Annually its your<br>choice</div>
    <div class="item" style="top:119px">Invoices entered and<br>bank accounts<br>reconciled</div>
    <div class="item" style="top:197px">Purchase and sales<br>ledgers reconciled</div>
    <div class="note software">All software is<br>included.</div>
    <div class="note support">Unlimited support<br>and assistance.</div>
  </div>
</section>

<section class="package insight">
  <div class="head">INSIGHT</div>
  <svg class="pointer" viewBox="0 0 34 28" aria-hidden="true"><path d="M0 0h34L17 28z" fill="var(--blue-tri)"/></svg>
  <div class="body">
    <div class="stripe"></div>
    <div class="item" style="top:36px">Monthly/Quarterly/<br>Annually its your<br>choice</div>
    <div class="item" style="top:101px">Book-keeping + :</div>
    <div class="item" style="top:141px">Accounting<br>adjustments to give a<br>true reflection of your<br>profit/loss to date</div>
    <div class="item" style="top:230px">Management<br>Accounts</div>
    <div class="item" style="top:281px">Regular meeting to<br>discuss business<br>performance and<br>possible areas for<br>improvement</div>
    <div class="note software">All software is<br>included.</div>
    <div class="note support">Unlimited support<br>and assistance.</div>
  </div>
</section>

<section class="package compliance">
  <div class="head">COMPLIANCE</div>
  <svg class="pointer" viewBox="0 0 34 28" aria-hidden="true"><path d="M0 0h34L17 28z" fill="var(--grey-tri)"/></svg>
  <div class="body">
    <div class="stripe"></div>
    <div class="item" style="top:36px">What every business<br>must do:</div>
    <div class="item" style="top:91px">Financial statements<br>prepared</div>
    <div class="item" style="top:145px">Income tax<br>computation</div>
    <div class="item" style="top:204px">Personal tax returns</div>
    <div class="note software">All software is<br>included.</div>
    <div class="note support">Unlimited support<br>and assistance.</div>
  </div>
</section>

<section class="package professional">
  <div class="head">PROFESSIONAL</div>
  <svg class="pointer" viewBox="0 0 34 28" aria-hidden="true"><path d="M0 0h34L17 28z" fill="var(--pink-tri)"/></svg>
  <div class="body">
    <div class="stripe"></div>
    <div class="item" style="top:36px">Bespoke solutions for<br>your business</div>
    <div class="item" style="top:91px">Business planning</div>
    <div class="item" style="top:145px">Cash flow planning<br>and forecasting</div>
    <div class="item" style="top:205px">Specialist tax planning</div>
    <div class="item" style="top:253px">Business turnaround</div>
    <div class="note software">All software is<br>included.</div>
    <div class="note support">Unlimited support<br>and assistance.</div>
  </div>
</section>

<section class="package payroll">
  <div class="head">PAYROLL</div>
  <svg class="pointer" viewBox="0 0 34 28" aria-hidden="true"><path d="M0 0h34L17 28z" fill="var(--lilac-tri)"/></svg>
  <div class="body">
    <div class="stripe"></div>
    <div class="item" style="top:36px">ETI</div>
    <div class="item" style="top:86px">Returns Weekly/<br>monthly</div>
    <div class="item" style="top:145px">UK/Channel Island</div>
  </div>
</section>

<p class="catchup">Many clients have a need for a "catch-up" project to get their books and accounts up to date.<br>We will agree with you a plan to complete the project at the outset and agree a fixed price.&nbsp; Interest free credit is</p>
</body>
</html>
```